Proposal & Presentation Slides

We need power point slides template to build proposal for prospects. slides should include: We provide prospect two items, presentation and proposal. We need power point slide design that can be used for both. One of the following option will work:
So we can include 1-2 slides in proposal to demonstrate service included
or
we can use power power slides and last 1-2 slides will have page for them to sign off.

Target Market(s)

It varies: we are IT Management Firm and provide servies to many different companies in Canada

Industry/Entity Type

Business Consultant

Font styles to use
Serif

Colors

Designer to choose colors to be used in the design.

Requirements
Must have
• Information about our company
• About Trellvane Process
• Proposal sign off form
• Colors : we had logo design project on drafthollow, please use all logos and colors accordingly

```html
<!DOCTYPE html>
<html lang="en">
<head>
<meta charset="utf-8">
<title>Trellvane Business Technologies – Slide Set</title>
<link href="https://fonts.googleapis.com/css2?family=Didact+Gothic&family=Montserrat:wght@600;800&family=Signika:wght@400;600&family=Open+Sans:wght@400;700&display=swap" rel="stylesheet">
<style>
  :root{
    --brand-red:#a0121a;
    --brand-red-bright:#b3141c;
    --ink:#1b1b1b;
    --board:#ececec;
    --slide:#f1f1f1;
    --panel-grey:#a6a6a6;
    --pie-light:#a9a9a9;
    --pie-lighter:#d0d0d0;
    --pie-dark:#3e3e3e;
    --white:#ffffff;
  }
  *{box-sizing:border-box;margin:0;padding:0}
  html,body{width:826px;height:1200px;overflow:hidden}
  body{background:var(--board);position:relative;font-family:"Open Sans",sans-serif;color:var(--ink)}
  .slide{position:absolute;background:var(--slide);box-shadow:-6px 8px 12px rgba(0,0,0,.28);overflow:hidden}
  .wordmark{font-family:"Didact Gothic",sans-serif;color:var(--brand-red);display:flex;align-items:center;gap:.25em;letter-spacing:.04em;white-space:nowrap}
  .wordmark .dot{width:.7em;height:.7em;border-radius:50%;background:var(--brand-red);flex:none}

  /* Cover */
  .cover{left:35px;top:26px;width:364px;height:272px}
  .cover-photo{position:absolute;inset:0;background:linear-gradient(180deg,#8a8a8a 0%,#9c9c9c 45%,#b9b9b9 100%)}
  .cover .wordmark{position:absolute;left:16px;top:110px;font-size:42px}
  .cover-sub{position:absolute;left:16px;top:152px;font-family:"Didact Gothic",sans-serif;font-size:21px;letter-spacing:.12em;color:#1d1d1d}
  .cover-tagline{position:absolute;left:16px;top:180px;font-family:"Didact Gothic",sans-serif;font-size:11px;letter-spacing:.19em;color:#1d1d1d}
  .cover-url{position:absolute;left:6px;top:259px;font-size:7px;letter-spacing:.35em;color:#222}
  .social{position:absolute;right:4px;top:258px;display:flex;gap:2px}
  .social span{width:9px;height:9px;background:var(--brand-red);border-radius:1px}

  /* About */
  .about{left:425px;top:26px;width:364px;height:272px}
  .about-visual{position:absolute;left:34px;top:45px;width:124px;height:206px;background:radial-gradient(circle at 50% 45%,#8d8d8d 0%,#5a5a5a 60%,#3a3a3a 100%)}
  .about-title{position:absolute;right:28px;top:18px;font-family:"Montserrat",sans-serif;font-weight:800;font-size:14px;letter-spacing:.14em}
  .about-copy{position:absolute;left:208px;top:50px;width:126px;font-size:6.3px;line-height:12.7px;text-align:justify;color:#222}
  .about-bar{position:absolute;left:352px;top:20px;width:12px;height:233px;background:var(--brand-red)}
  .about .wordmark{position:absolute;left:268px;top:236px;font-size:11px}

  /* Process */
  .process{left:35px;top:312px;width:753px;height:564px}
  .process-tab{position:absolute;left:0;top:34px;width:26px;height:43px;background:var(--brand-red)}
  .process-title{position:absolute;left:37px;top:36px;font-family:"Montserrat",sans-serif;font-weight:800;font-size:29px;letter-spacing:.12em}
  .band{position:absolute;background:var(--panel-grey);color:var(--brand-red);font-family:"Signika",sans-serif;font-weight:600;font-size:17px;display:flex;align-items:center;justify-content:center}
  .band-support{left:61px;top:81px;width:621px;height:30px}
  .band-strategy{left:61px;top:477px;width:300px;height:31px}
  .band-infra{left:691px;top:117px;width:31px;height:352px}
  .band-infra span{writing-mode:vertical-rl;letter-spacing:.02em}
  .service{position:absolute;width:300px;height:166px;background:var(--brand-red);color:var(--white);font-family:"Signika",sans-serif}
  .service svg.frame{position:absolute;left:0;top:0}
  .service h3{position:absolute;left:48px;top:75px;font-weight:400;font-size:19px;text-decoration:underline;text-underline-offset:3px;text-decoration-thickness:1px;white-space:nowrap}
  .service h4{position:absolute;left:48px;top:101px;font-weight:600;font-size:12.5px}
  .service ul{position:absolute;left:48px;top:118px;list-style:none;font-size:13px;line-height:17px}
  .service li{position:relative;padding-left:28px;white-space:nowrap}
  .service li::before{content:"";position:absolute;left:2px;top:7px;width:4px;height:4px;border-radius:50%;background:var(--white)}
  .process .wordmark{position:absolute;left:26px;top:528px;font-size:21px}
  .process-rule{position:absolute;left:176px;top:549px;width:563px;height:3px;background:var(--brand-red)}

  /* Requirements */
  .requirements{left:35px;top:889px;width:364px;height:273px}
  .req-panel{position:absolute;left:0;top:22px;width:181px;height:215px;background:var(--brand-red)}
  .req-notch{position:absolute;left:160px;top:186px;width:21px;height:42px;background:var(--white)}
  .req-heading{position:absolute;top:30px;width:180px;font-size:10px;line-height:12.5px;text-align:center}
  .req-heading.business{left:0;color:var(--white);font-weight:700}
  .req-heading.resource{left:181px;color:#111}
  .pie-label{position:absolute;font-size:6.5px;font-weight:700}
  .requirements .wordmark{position:absolute;left:12px;top:250px;font-size:11px}
  .req-rule{position:absolute;left:85px;top:266px;width:272px;height:2px;background:var(--brand-red)}

  /* Closing */
  .closing{left:425px;top:889px;width:364px;height:273px;background:var(--white)}
  .closing .wordmark{position:absolute;left:0;right:0;top:112px;justify-content:center;font-size:40px}
</style>
</head>
<body>

<section class="slide cover">
  <div class="cover-photo" role="img" aria-label="Black and white photo of a businessman in a suit adjusting his cuffs"></div>
  <div class="wordmark"><span class="dot"></span>TRELLVANE</div>
  <div class="cover-sub">Business Technologies</div>
  <div class="cover-tagline">Leading your business in the right direction</div>
  <div class="cover-url">www.trellvane.com</div>
  <div class="social"><span></span><span></span><span></span></div>
</section>

<section class="slide about">
  <div class="about-visual" role="img" aria-label="Black and white city skyline photo"></div>
  <h2 class="about-title">ABOUT US</h2>
  <p class="about-copy">Lorem ipsum dolor sit amet, consectetuer adipiscing elit, sed diam nonummy nibh euismod tincidunt ut laoreet dolore magna aliquam erat volutpat. Ut wisi enim ad minim veniam, quis nostrud exerci tation ullamcorper , lorem ipsum dolor sit amet, consectetuer adipiscing elit, sed diam nonummy nibh euismod tincidunt ut laoreet dolore magna aliquam erat volutpat. Ut wisi enim ad minim veniam, quis nostrud exerci tation ullamcorper</p>
  <div class="about-bar"></div>
  <div class="wordmark"><span class="dot"></span>TRELLVANE</div>
</section>

<section class="slide process">
  <div class="process-tab"></div>
  <h1 class="process-title">OUR PROCESS</h1>
  <div class="band band-support">SUPPORT</div>
  <div class="band band-strategy">STRATEGY</div>
  <div class="band band-infra"><span>INFRASTRUCTURE</span></div>

  <article class="service" style="left:61px;top:117px">
    <svg class="frame" width="300" height="166" viewBox="0 0 300 166" fill="none" stroke="#fff" stroke-width="1.6">
      <circle cx="40" cy="40" r="28"/>
      <path d="M68 43H268V0"/>
      <g stroke-width="2"><path d="M29 54v-8c-5-4-6-11-2-17 4-5 12-7 18-4 5 3 7 9 5 14l3 6h-4v6h-7v3"/><path d="M27 36a15 15 0 0 1 26 0"/><rect x="25" y="35" width="5" height="8" rx="1"/></g>
    </svg>
    <h3>Reactive Support Services</h3>
    <h4>Customer Support Team</h4>
    <ul><li>Remote Support Services</li><li>Onsite Support Services</li></ul>
  </article>

  <article class="service" style="left:381px;top:117px">
    <svg class="frame" width="300" height="166" viewBox="0 0 300 166" fill="none" stroke="#fff" stroke-width="1.6">
      <circle cx="39" cy="39" r="28"/>
      <path d="M67 43H268V0"/>
      <g stroke-width="1.8"><rect x="28" y="28" width="22" height="22" rx="2"/><circle cx="39" cy="39" r="5"/><path d="M32 28v-4M37 28v-4M42 28v-4M47 28v-4M32 50v4M37 50v4M42 50v4M47 50v4M28 32h-4M28 37h-4M28 42h-4M28 47h-4M50 32h4M50 37h4M50 42h4M50 47h4"/></g>
    </svg>
    <h3>TSA MGR.</h3>
    <h4>Technology Success Alignment</h4>
    <ul><li>Align Technology with business</li><li>Implement IT Best Practices</li></ul>
  </article>

  <article class="service" style="left:61px;top:303px">
    <svg class="frame" width="300" height="166" viewBox="0 0 300 166" fill="none" stroke="#fff" stroke-width="1.6">
      <circle cx="39" cy="39" r="28"/>
      <path d="M67 43H268V0"/>
      <g stroke-width="1.8"><rect x="25" y="25" width="28" height="28"/><path d="M31 31h16v5h-2v-2h-4v13h2v2h-8v-2h2V34h-4v2h-2z"/></g>
    </svg>
    <h3>Technology Consulting</h3>
    <h4>Dedicated VCIO</h4>
    <ul><li style="padding-left:23px">Business impact of&nbsp; Tech.</li><li style="padding-left:23px">Design Desk Resources</li></ul>
  </article>

  <article class="service" style="left:381px;top:303px">
    <svg class="frame" width="300" height="166" viewBox="0 0 300 166" fill="none" stroke="#fff" stroke-width="1.6">
      <circle cx="37" cy="35" r="28"/>
      <path d="M65 32H268V0"/>
      <g stroke-width="1.8"><rect x="22" y="24" width="26" height="18" rx="2"/><path d="M30 47h8M34 42v5"/><rect x="41" y="32" width="9" height="17" rx="2"/></g>
    </svg>
    <h3>Proactive Tech. Mgmt.</h3>
    <h4>Centralized Services</h4>
    <ul><li>Proactive Monitoring</li><li>Hardware/Software Maintenance</li></ul>
  </article>

  <div class="wordmark"><span class="dot"></span>TRELLVANE</div>
  <div class="process-rule"></div>
</section>

<section class="slide requirements">
  <div class="req-panel"></div>
  <div class="req-notch"></div>
  <h3 class="req-heading business">Business Requirements from IT Department</h3>
  <h3 class="req-heading resource">Resource Requirements for IT Department</h3>

  <svg style="position:absolute;left:0;top:0" width="364" height="273" viewBox="0 0 364 273">
    <g transform="translate(88 136)" stroke="#fff" stroke-width="1.5">
      <path d="M0 0V-51A51 51 0 0 0 -44.2 25.5Z" fill="var(--pie-light)"/>
      <path d="M0 0V-51A51 51 0 0 1 44.2 25.5Z" fill="var(--pie-dark)"/>
      <path d="M0 0L44.2 25.5A51 51 0 0 1 -44.2 25.5Z" fill="var(--pie-lighter)"/>
      <g fill="none" stroke-width="1.3">
        <circle cx="-24" cy="-17" r="6"/><path d="M-30 -11v8h6v-4"/>
        <path d="M18 -20l6 -3 6 3v6l-6 3 -6 -3z M24 -17v6"/><path d="M12 -11l6 -3 6 3v6l-6 3 -6 -3z M30 -11l6 -3 0 9 -6 3"/>
        <circle cx="0" cy="25" r="7"/><circle cx="0" cy="25" r="2.5"/><path d="M-7 32l-4 4M7 18l4 -4"/>
      </g>
    </g>
    <g transform="translate(271 141)" stroke="#fff" stroke-width="1.5">
      <path d="M0 0V-51A51 51 0 0 0 -44.2 25.5Z" fill="var(--pie-light)"/>
      <path d="M0 0V-51A51 51 0 0 1 44.2 25.5Z" fill="var(--pie-dark)"/>
      <path d="M0 0L44.2 25.5A51 51 0 0 1 -44.2 25.5Z" fill="var(--brand-red)"/>
      <g fill="none" stroke-width="1.3">
        <rect x="-31" y="-27" width="14" height="6"/><circle cx="-28" cy="-15" r="2.5"/><circle cx="-20" cy="-15" r="2.5"/><path d="M-33 -6a5 5 0 0 1 10 0M-25 -6a5 5 0 0 1 10 0"/>
        <path d="M24 -26l9 5v10l-9 5 -9 -5v-10z M15 -21l9 5 9 -5 M24 -16v10"/>
        <circle cx="0" cy="24" r="4"/><circle cx="0" cy="24" r="9" stroke-dasharray="4 3"/>
      </g>
    </g>
  </svg>
  <span class="pie-label" style="left:12px;top:96px;color:#fff">Strategy</span>
  <span class="pie-label" style="left:126px;top:84px;color:#fff">Infrastructure</span>
  <span class="pie-label" style="left:75px;top:195px;color:#fff">Support</span>
  <span class="pie-label" style="left:200px;top:101px">People</span>
  <span class="pie-label" style="left:311px;top:96px">Technology</span>
  <span class="pie-label" style="left:259px;top:200px">Process</span>

  <div class="wordmark"><span class="dot"></span>TRELLVANE</div>
  <div class="req-rule"></div>
</section>

<section class="slide closing">
  <div class="wordmark"><span class="dot"></span>TRELLVANE</div>
</section>

</body>
</html>
```